Website Redesign - Spa Barn Outlet

We need a new website for a hot tub dealer. This is a redesign of the existing site. The goal of the site is to drive phone calls and emails to book warehouse viewings, not to sell inventory from the website. The dealer sells both new and used hot tubs. I'd like to see some of the big name brands reflected; he's a small dealer and needs trust factor. He also has a great rating with FTC. We are no longer going to use the site to list inventory. This is a lead generation site. The existing site is boring. We would like to see some imagination. The client has a rustic back woods warehouse. He's a very knowledgeable yet quirky client. He doesn't want people showing up thinking that this is a big box fancy dealership. He's like the Pricemart warehouse of hot tub dealers and the site should reflect that. No frills, honest advice, etc. www.spabarnoutlet.net

Target Market(s)

Surrey, Langley, Vancouver and area homeowners looking for new and used hot tubs

Number of Pages Required

5+ page

Font styles to use
Serif
Sans Serif

Colors

Designer to choose colors to be used in the design.

Requirements
Must have
• Home page

```html
<!DOCTYPE html>
<html lang="en">
<head>
<meta charset="utf-8">
<title>Spa Barn Outlet – Home</title>
<link href="https://fonts.googleapis.com/css2?family=Montserrat:wght@400;600;700;800&family=Open+Sans:wght@400;600;700&display=swap" rel="stylesheet">
<style>
:root{
  --blue:#1e9be0;
  --blue-dark:#1478b8;
  --ink:#222426;
  --panel:#2a2c2e;
  --panel-soft:#3a3c3f;
  --grey-bg:#f3f3f3;
  --text:#6b6f73;
  --white:#ffffff;
  --footer:#1b2228;
}
*{margin:0;padding:0;box-sizing:border-box}
html,body{width:1200px;height:3772px;overflow:hidden}
body{position:relative;background:var(--white);font-family:"Open Sans",Arial,sans-serif;color:var(--text);font-size:13px;line-height:1.6}
h1,h2,h3,h4,.nav,.btn{font-family:"Montserrat",Arial,sans-serif}
section,header,footer{position:absolute;left:0;width:1200px}
.container{position:absolute;left:160px;width:880px}
.btn{display:inline-block;font-size:12px;font-weight:600;letter-spacing:1px;text-transform:uppercase;border-radius:20px;padding:10px 26px}

/* hero */
.hero{top:0;height:760px;overflow:hidden}
.hero-photo{position:absolute;inset:0;background:linear-gradient(160deg,#5d6b4e 0%,#8a6a55 30%,#c9a28f 55%,#a56f66 75%,#4d3a33 100%)}
.hero-photo::after{content:"";position:absolute;inset:0;background:rgba(20,20,20,.35)}
.topline{top:6px;height:20px;font-size:11px;color:#e8e8e8;white-space:nowrap}
.masthead{top:28px;height:60px;background:var(--white);display:flex;align-items:center;justify-content:space-between;padding:0 20px}
.brand{font-family:"Montserrat",Arial,sans-serif;font-weight:800;font-size:22px;color:var(--blue-dark);display:flex;align-items:center;gap:8px;white-space:nowrap;line-height:1}
.brand-mark{width:14px;height:14px;background:var(--blue)}
.nav{display:flex;gap:16px;font-size:10.5px;font-weight:600;color:#444;text-transform:uppercase;align-items:center;white-space:nowrap}
.hero-copy{top:250px;text-align:center;color:var(--white)}
.hero-copy h1{font-size:50px;font-weight:800;letter-spacing:1px}
.hero-copy p{font-size:15px;letter-spacing:3px;font-weight:600;margin-top:6px}
.hero-copy .btn{margin-top:28px;border:2px solid rgba(255,255,255,.7);color:var(--white);background:rgba(0,0,0,.25)}

/* services */
.services{top:580px;height:250px}
.services .container{display:flex;justify-content:space-between}
.service{position:relative;width:280px;height:240px;background:var(--panel);color:#c9cbcd;text-align:center;padding:70px 28px 0;margin-top:28px}
.service .icon{position:absolute;top:-28px;left:112px;width:56px;height:56px;border-radius:50%;background:var(--blue);border:5px solid rgba(255,255,255,.5);display:flex;align-items:center;justify-content:center}
.service h3{color:var(--white);font-size:16px;font-weight:700;letter-spacing:1px;margin-bottom:14px}
.service p{font-size:12px}

/* why */
.why{top:940px;height:400px;border-bottom:1px solid #e3e3e3}
.section-title{text-align:center;font-size:24px;font-weight:700;color:var(--ink);letter-spacing:1px}
.section-title::after{content:"";display:block;width:40px;height:3px;background:var(--blue);margin:12px auto 0}
.why-grid{top:100px;display:grid;grid-template-columns:1fr 64px 64px 1fr;column-gap:22px;row-gap:50px}
.why-item h3{font-size:17px;font-weight:700;color:var(--ink);margin-bottom:8px}
.why-item p{font-size:12px}
.why-item.left{text-align:right}
.why-icon{width:64px;height:64px;border:1px solid #dcdcdc;display:flex;align-items:center;justify-content:center}

/* about */
.about{top:1340px;height:448px;background:var(--grey-bg)}
.about-photos{position:absolute;left:208px;top:62px;width:320px;display:grid;grid-template-columns:155px 155px;gap:10px}
.about-photos div{height:128px}
.ph1{background:linear-gradient(135deg,#8b7965,#c8b7a0)}
.ph2{background:linear-gradient(135deg,#6f6152,#a18b74)}
.ph3{background:linear-gradient(135deg,#a7b4b8,#e3e7e6)}
.ph4{background:linear-gradient(135deg,#7a8f96,#c3d1d3)}
.about-copy{position:absolute;left:588px;top:70px;width:400px}
.about-copy h2{font-size:40px;font-weight:800;color:var(--ink);line-height:1}
.about-copy h3{font-size:20px;font-weight:700;color:var(--ink);margin:6px 0 18px}
.about-copy .lead{color:var(--ink);font-weight:600;margin-bottom:10px}
.about-copy p{font-size:12px;margin-bottom:10px}
.about-copy .btn{background:var(--blue);color:var(--white);margin-top:8px}

/* process */
.process{top:1788px;height:432px;overflow:hidden}
.process-photo{position:absolute;inset:0;background:linear-gradient(100deg,#0c5d95 0%,#1a8fd0 45%,#3aa9e2 70%,#0f6aa6 100%)}
.process-photo::after{content:"";position:absolute;inset:0;background:rgba(10,60,110,.3)}
.process .section-title{position:absolute;top:70px;width:1200px;color:var(--white)}
.process .section-title::after{background:var(--white)}
.steps{top:170px;display:flex;justify-content:space-between}
.step{width:208px;height:208px;border-radius:50%;background:var(--ink);color:#bfc1c3;text-align:center;padding:58px 26px 0}
.step h4{color:var(--white);font-size:13px;font-weight:700;letter-spacing:1px;margin-bottom:10px}
.step h4 span{font-size:28px;margin-right:6px;vertical-align:-3px}
.step p{font-size:11px;line-height:1.5}

/* articles */
.articles{top:2280px;height:720px}
.articles-label{position:absolute;left:188px;top:50px;font-family:"Montserrat",Arial,sans-serif;font-weight:700;color:var(--ink);font-size:20px;letter-spacing:1px}
.articles-label::after{content:"";display:inline-block;width:40px;height:2px;background:var(--blue);margin-left:14px;vertical-align:middle}
.vertical-word{position:absolute;left:150px;top:160px;transform:rotate(-90deg);transform-origin:left top;font-family:"Montserrat",Arial,sans-serif;font-weight:700;color:var(--ink);font-size:20px;letter-spacing:2px}
.article-photo{position:absolute;left:180px;top:80px;width:360px;height:600px;background:linear-gradient(180deg,#e9ecee 0%,#cfd6da 55%,#b5bdc1 100%)}
.feature{position:absolute;left:540px;top:112px;width:500px;height:168px;background:var(--panel);padding:24px 30px;color:#c0c2c4}
.feature h3{color:var(--blue);font-size:18px;font-weight:700;margin-bottom:10px}
.feature p{font-size:12px}
.article-list{position:absolute;left:540px;top:290px;width:500px;background:var(--white);border:1px solid #e6e6e6;padding:14px 26px}
.article-item{display:flex;gap:16px;padding:16px 0;border-bottom:1px solid #ececec}
.article-item:last-child{border-bottom:none}
.article-item .icon{flex:none;width:44px;height:44px;background:var(--blue);display:flex;align-items:center;justify-content:center}
.article-item h4{font-size:12px;font-weight:700;color:var(--blue);margin-bottom:4px}
.article-item p{font-size:11.5px;line-height:1.5}

/* testimonials */
.testimonials{top:3000px;height:380px}
.testimonials h2{position:absolute;left:160px;top:20px;font-size:24px;font-weight:700;color:var(--ink)}
.testimonials h2::after{content:"";display:block;width:40px;height:3px;background:var(--blue);margin-top:10px}
.quotes{top:120px;display:flex;justify-content:space-between}
.quote{width:420px;display:flex;gap:22px}
.quote .who{flex:none;width:90px;text-align:center}
.avatar{width:70px;height:70px;border-radius:50%;background:linear-gradient(135deg,#b89580,#6e5647);margin:0 auto 8px}
.who h4{font-size:12px;color:var(--ink);font-weight:700}
.who span{font-size:11px}
.quote blockquote{font-size:12px;border-left:2px solid #e2e2e2;padding-left:18px;font-style:italic;position:relative}
.quote blockquote::before{content:"“";position:absolute;left:-8px;top:-26px;font-size:40px;color:#cfd2d4;font-style:normal}
.dots{position:absolute;top:310px;width:1200px;display:flex;justify-content:center;gap:8px}
.dots i{width:10px;height:10px;border-radius:50%;background:#c7cacc}
.dots i:first-child{background:var(--blue)}

/* cta */
.cta{top:3380px;height:100px;background:var(--blue);color:var(--white)}
.cta .container{top:24px;display:flex;justify-content:space-between;align-items:center}
.cta h2{font-size:24px;font-weight:700}
.cta p{font-size:12px;font-weight:600;letter-spacing:.5px}
.cta .btn{background:var(--ink);color:var(--white);border-radius:3px}

/* footer */
.site-footer{top:3480px;height:292px;background:var(--footer);color:#9aa1a6;text-align:center}
.footer-brand{position:absolute;top:40px;width:1200px;display:flex;justify-content:center}
.footer-brand .brand{background:var(--white);padding:10px 18px}
.subscribe{position:absolute;top:110px;left:400px;width:400px;display:flex}
.subscribe span{flex:1;height:40px;background:var(--white);border-radius:20px 0 0 20px;text-align:left;padding:10px 18px;color:#999;font-size:12px}
.subscribe b{width:90px;height:40px;background:var(--blue);color:var(--white);border-radius:0 20px 20px 0;font-family:"Montserrat",Arial,sans-serif;font-size:12px;padding-top:11px}
.footer-nav{position:absolute;top:176px;width:1200px;display:flex;justify-content:center;gap:30px;font-size:11px;font-weight:600;text-transform:uppercase;color:#c7ccd0}
.social{position:absolute;top:210px;width:1200px;display:flex;justify-content:center;gap:10px}
.social i{width:26px;height:26px;border-radius:50%;background:#3a444c}
.copyright{position:absolute;top:258px;width:1200px;font-size:11px}
</style>
</head>
<body>

<header class="hero">
  <div class="hero-photo" role="img" aria-label="Woman relaxing in a hot tub with flower petals in a garden spa"></div>
  <div class="container topline">sales@spabarnoutlet.net &nbsp;|&nbsp; Call Today: 604-555-0148</div>
  <div class="container masthead">
    <div class="brand"><span class="brand-mark"></span>Spa Barn Outlet</div>
    <nav class="nav">
      <span>Home</span><span>About Hot Tubs</span><span>Used Hot Tubs</span><span>Custom Build</span><span>Testimonials</span><span>Reviews</span><span>Contact</span>
      <svg width="12" height="12" viewBox="0 0 12 12"><circle cx="5" cy="5" r="3.8" fill="none" stroke="#444" stroke-width="1.6"/><line x1="8" y1="8" x2="11.5" y2="11.5" stroke="#444" stroke-width="1.6"/></svg>
    </nav>
  </div>
  <div class="container hero-copy">
    <h1>ALL 2016 TUBS MUST GO!</h1>
    <p>ONE YEAR EXTENDED WARRANTY ON ALL NEW TUBS</p>
    <span class="btn">Call us on: 604-555-0148</span>
  </div>
</header>

<section class="services">
  <div class="container">
    <article class="service">
      <div class="icon"><svg width="24" height="24" viewBox="0 0 24 24" fill="none" stroke="#fff" stroke-width="2"><path d="M12 3l4 6H8zM4 18l3-6 3 5zM20 18h-7l3-6z"/></svg></div>
      <h3>RECYCLING</h3>
      <p>We take away your old hot tub and recycle every usable part, so nothing ends up in the landfill and you save on disposal fees.</p>
    </article>
    <article class="service">
      <div class="icon"><svg width="24" height="24" viewBox="0 0 24 24" fill="none" stroke="#fff" stroke-width="2"><circle cx="12" cy="12" r="4"/><path d="M12 2v4M12 18v4M2 12h4M18 12h4M5 5l3 3M16 16l3 3M19 5l-3 3M8 16l-3 3"/></svg></div>
      <h3>PARTS</h3>
      <p>Pumps, heaters, covers and filters for most makes are kept in our warehouse, with honest advice on what your tub really needs.</p>
    </article>
    <article class="service">
      <div class="icon"><svg width="24" height="24" viewBox="0 0 24 24" fill="none" stroke="#fff" stroke-width="2"><path d="M14 6a4 4 0 0 0 5 5l-9 9-3-3 9-9a4 4 0 0 0-2-2z"/></svg></div>
      <h3>REPAIR</h3>
      <p>Our service techs repair leaks, electrical faults and jets on site across Surrey, Langley and Vancouver at fair local rates.</p>
    </article>
  </div>
</section>

<section class="why">
  <h2 class="section-title" style="position:absolute;top:30px;width:1200px">WHY CHOOSE US</h2>
  <div class="container why-grid">
    <div class="why-item left"><h3>FAST BUILDING</h3><p>Custom tubs are built and delivered quickly, with clear timelines and no surprises along the way.</p></div>
    <div class="why-icon"><svg width="26" height="26" viewBox="0 0 26 26" fill="none" stroke="#1e9be0" stroke-width="2"><circle cx="13" cy="14" r="9"/><path d="M13 9v5l3 3M10 3h6"/></svg></div>
    <div class="why-icon"><svg width="26" height="26" viewBox="0 0 26 26" fill="none" stroke="#1e9be0" stroke-width="2"><rect x="4" y="4" width="18" height="18" rx="2"/><path d="M9 13h8M13 9v8"/></svg></div>
    <div class="why-item"><h3>SAVE MONEY</h3><p>Warehouse pricing on new and used hot tubs, because we skip the fancy showroom costs.</p></div>
    <div class="why-item left"><h3>HIGH PRESTIGE</h3><p>We carry trusted big name brands and stand behind every tub with real warranties.</p></div>
    <div class="why-icon"><svg width="26" height="26" viewBox="0 0 26 26"><path d="M13 3l3 7 7 .5-5.5 4.5 2 7-6.5-4-6.5 4 2-7L3 10.5 10 10z" fill="#1e9be0"/></svg></div>
    <div class="why-icon"><svg width="26" height="26" viewBox="0 0 26 26" fill="none" stroke="#1e9be0" stroke-width="2"><path d="M5 21l3-1 12-12-2-2L6 18zM15 7l4 4"/></svg></div>
    <div class="why-item"><h3>CREATIVE PLAN</h3><p>We help plan the right spot, power and base for your backyard before the tub arrives.</p></div>
  </div>
</section>

<section class="about">
  <div class="about-photos">
    <div class="ph1" role="img" aria-label="Wooden hot tub on a deck"></div>
    <div class="ph2" role="img" aria-label="Bathroom with soaking tub"></div>
    <div class="ph3" role="img" aria-label="Modern white bathroom with tub"></div>
    <div class="ph4" role="img" aria-label="Spa tub by a window"></div>
  </div>
  <div class="about-copy">
    <h2>WE ARE</h2>
    <h3>SPA BARN OUTLET</h3>
    <p class="lead">Over 200 hot tubs in stock, both new and used, from our backwoods warehouse!</p>
    <p>No sales floor glitz, just rows of tubs you can sit in, test and compare. We give straight answers and fair prices on every model.</p>
    <p>Come by for a warehouse viewing and talk to a tub expert who knows every pump and panel. Call or email to book your visit today.</p>
    <span class="btn">Read More</span>
  </div>
</section>

<section class="process">
  <div class="process-photo" role="img" aria-label="Woman resting in a blue lit hot tub"></div>
  <h2 class="section-title">OUR PROCESS</h2>
  <div class="container steps">
    <div class="step"><h4><span>01</span>MEET</h4><p>Call or email us to book a warehouse viewing at a time that suits you.</p></div>
    <div class="step"><h4><span>02</span>DISCUSSION</h4><p>We talk about your space, budget and how you plan to use your tub.</p></div>
    <div class="step"><h4><span>03</span>IDEAL</h4><p>Test the tubs and pick the one that fits your home and family.</p></div>
    <div class="step"><h4><span>04</span>CONTRACT</h4><p>Sign a simple agreement and we deliver and set up your hot tub.</p></div>
  </div>
</section>

<section class="articles">
  <div class="vertical-word">OUR</div>
  <div class="articles-label">ARTICLES</div>
  <div class="article-photo" role="img" aria-label="Freestanding bathtub beside a bright curtained window"></div>
  <div class="feature">
    <h3>PHASELLUS QUIS FINIBUS MI</h3>
    <p>Sed ut perspiciatis unde omnis iste natus error sit voluptatem accusantium doloremque laudantium, totam rem aperiam, eaque ipsa quae ab illo inventore veritatis et quasi architecto beatae vitae dicta sunt explicabo.</p>
  </div>
  <div class="article-list">
    <div class="article-item">
      <div class="icon"><svg width="20" height="20" viewBox="0 0 20 20" fill="none" stroke="#fff" stroke-width="2"><path d="M3 10l5 5 9-10"/></svg></div>
      <div><h4>FUSCE ETIAM NIBH</h4><p>Nemo enim ipsam voluptatem quia voluptas sit aspernatur aut odit aut fugit, sed quia consequuntur magni dolores.</p></div>
    </div>
    <div class="article-item">
      <div class="icon"><svg width="20" height="20" viewBox="0 0 20 20" fill="none" stroke="#fff" stroke-width="2"><path d="M3 10l5 5 9-10"/></svg></div>
      <div><h4>FUSCE ETIAM NIBH</h4><p>Neque porro quisquam est qui dolorem ipsum quia dolor sit amet, consectetur adipisci velit sed quia non numquam.</p></div>
    </div>
    <div class="article-item">
      <div class="icon"><svg width="20" height="20" viewBox="0 0 20 20" fill="none" stroke="#fff" stroke-width="2"><path d="M3 10l5 5 9-10"/></svg></div>
      <div><h4>FUSCE ETIAM NIBH</h4><p>Ut enim ad minima veniam, quis nostrum exercitationem ullam corporis suscipit laboriosam nisi ut aliquid ex ea.</p></div>
    </div>
  </div>
</section>

<section class="testimonials">
  <h2>TESTIMONIAL</h2>
  <div class="container quotes">
    <div class="quote">
      <div class="who"><div class="avatar" role="img" aria-label="Customer portrait"></div><h4>Dana Morrow</h4><span>Surrey</span></div>
      <blockquote>No pushy sales, just honest advice. We tried five tubs in the warehouse and went home with a great used model at a fair price.</blockquote>
    </div>
    <div class="quote">
      <div class="who"><div class="avatar" role="img" aria-label="Customer portrait"></div><h4>Glen Archer</h4><span>Langley</span></div>
      <blockquote>The team knew every brand inside out. Delivery was quick and they even took our old tub away for recycling.</blockquote>
    </div>
  </div>
  <div class="dots"><i></i><i></i><i></i><i></i></div>
</section>

<section class="cta">
  <div class="container">
    <div>
      <h2>SCHEDULE AN APPOINTMENT TODAY!</h2>
      <p>COME BY FOR A VIEWING OF OUR HUGE RANGE OF NEW AND USED HOT TUBS.</p>
    </div>
    <span class="btn">Contact Now</span>
  </div>
</section>

<footer class="site-footer">
  <div class="footer-brand"><div class="brand">Spa Barn Outlet</div></div>
  <div class="subscribe"><span>Your email address</span><b>SEND</b></div>
  <nav class="footer-nav"><span>Home</span><span>About Hot Tubs</span><span>Used Hot Tubs</span><span>Testimonials</span><span>Reviews</span><span>Contact</span></nav>
  <div class="social"><i></i><i></i><i></i></div>
  <p class="copyright">© 2016 Spa Barn Outlet. All rights reserved. www.spabarnoutlet.net</p>
</footer>

</body>
</html>
```